New small software startup needs a web design!

Hi! I need a talented web designer to design the overall visual look & feel & navigation of my website.
Just images and basic HTML of course; this is a website design contest not so much a coding contest (although using PHP for "include()" etc might be good!), although yes I have paid the extra $150 for a "Coded Website"

GENERAL OVERVIEW:
-----------------
My new startup company is very simple - I develop and sell shareware apps for Windows.
The software I develop is low-level system & security, so keep that in mind when designing the look & feel of the website.
My website which you are designing for is for hosting the company and showcasing the software.

So it's not a very complicated website, and has a very basic layout/structure.

Most of the webpages I need you to design will essentially just have "blank content" of course, so you don't need to worry about many technicalities, mostly just the LOOK & FEEL & NAVIGATION.

So as you can probably already imagine, it needs things like:
- Download page
- Shop page where they can click links to purchase
- About page where they can read FAQ/Privacy Policy/Terms Of Use, or Contact me
- Members area for registered users to login, where they can download and get tech support
- a subdirectory for each software application to show each off on its own (eg. /software/app1/index.htm)
- a page where i can offer a one-page summary of my products in different foreign languages

IMPORTANT:
----------
- HTML4 ONLY (no HTML5)
- Must support Firefox, Internet Explorer, and Chrome
- CSS is good, although you dont have to use it if you dont want to or feel it's unnecessary
- NO ACTIVE CONTENT (no Flash or Java etc)
- NO SCRIPTS (no Javascript or VBScript etc)
- The overall type of look/feel i'm after is "CLEAN, PROFESSIONAL, TECHNICAL" (but not overcomplicated)
- You must incorporate the company logo - see Attached file.
(You're free to use Photoshop etc to modify the logo how you see fit, for example to resize its elements, or to change the location of the company name part of it, or to remove part of it, change background/transparency, etc etc)
- Although ive named all files here .HTM i'll actually be using PHP, so feel free to use .PHP names also, but .HTM is fine also
- You're also free to use server-side PHP if you wish, for example to include() files such as footer.htm
- Please use Photoshop for designing the images - i'll naturally be needing all PSD files
- Please only use fonts that can be used commercially. The font we use in our logo is 'Good Times' in case you're wondering, although I'm not suggesting one way or the other to use it or not for the website - just because it looks good in the logo may not necessarily mean it works for the rest of the website. Then again, maybe it does, i dont know.

BASIC WEBSITE DIRECTORY STRUCTURE:
----------------------------------
These are the files you should be sending me. Most of these can just be essentially blank pages in regards to content (or with some "dummy filler" text/images), although most (including most "blanks") will obviously have hyperlinks to other pages.
But obviously each page even the blank ones will still have main menu etc.

In no particular order:
---
/index.htm "Welcome to Quorvanta..."
/books/index.htm "Select a book category..."
/books/cat1/index.htm - List of books in cat1
/books/cat2/index.htm - List of books in cat2
/members.htm Username & pass login page. Also acts as the Unsuccessful page.
/members/index.htm - Successfully logged in
/members/download.htm - Members-only downloads
/members/support.htm - Members-only support (basically just a clone of /about/contact.htm)
/about/index.htm "About Quorvanta..."
/about/contact.htm "Contact Us..."
/about/privacy.htm "Privacy Statement"
/about/termsofuse.htm "Terms of Use"
/about/resellers.htm "Information for Resellers"
/lang/index.htm "Select language..."
/lang/fr/index.htm - French products summary page
/lang/es/index.htm - Spanish products summary page
/software/index.htm "Select a program to find out more about it..."
/software/support.htm "Technical support"
/software/shop.htm "Select a program to buy..."
/software/download.htm "Select a program to download..."
/software/app1/index.htm Main "About" page for Application #1
/software/app1/download.htm - Download page for App 1
/software/app1/features.htm - Features page for App 1
/software/app1/screenshots.htm - Screenshots page for App 1
/software/app1/support.htm - Support page for App 1
/software/app1/purchase.htm - Purchase page for App 1
/software/app2/index.htm (clone of App 1)
/software/app2/download.htm "
/software/app2/screenshots.htm "
/software/app2/support.htm "
/software/app2/purchase.htm "
/misc/footer.htm A footer that all other pages also include() -- see below for details

---

MAIN MENU (available from every page):
Home (/index.htm)
Software (/software/index.htm)
Shop (/software/shop.htm)
Books (/books/index.htm)
Members (/members.htm)
Resellers (/about/resellers.htm)
Support (/software/support.htm)
About (/about/index.htm)

FOOTER (every page) for the smallprint:
"Copyright (C) 2015. All rights reserved."
as well as hyperlinks to "Privacy Policy", "Terms of Use", "Contact"

MEMBERS AREA:
The Members subarea also has an extra submenu:
Home (/members/index.htm)
Download (/members/download.htm)
Support (/members/support.htm)

APPLICATION AREA:
Each Application subarea also has an extra submenu:
Home (/software/app1/index.htm)
Features (/software/app1/features.htm)
Download (/software/app1/download.htm)
Support (/software/app1/support.htm)
Purchase (/software/app1/purchase.htm)
Screenshots (/software/app1/screenshots.htm)

Obviously it would be best to have one single FOOTER.HTM that every other HTM file can link to, rather than having the footer in every file (I'll be using PHP so its easy to "include(footer.htm)")

--
Thankyou for taking on my design challenge, and I wish you best of luck and a great design! :)

Target Market(s)

General users of Windows operating system who use system & security tools

Industry/Entity Type

Computer Software

Coding

Coded - Design and coding required

Number of Pages Required

5+ page

Font styles to use
Serif
Sans Serif

Requirements
Must have
• See project description
Should not have
• See project description

```html
<!DOCTYPE html>
<html lang="en">
<head>
<meta charset="utf-8">
<title>Quorvanta — System &amp; Security Software</title>
<link rel="stylesheet" href="https://fonts.googleapis.com/css2?family=Open+Sans:wght@400;600;700;800&display=swap">
<style>
:root{
  --blue:#1b7fc9;
  --blue-dark:#0f4f86;
  --navy:#123a61;
  --red:#d8342c;
  --slate:#3b4856;
  --ink:#333a42;
  --muted:#7a838c;
  --light:#f1f3f5;
  --line:#dfe3e7;
  --footer:#1f252c;
  --footer-deep:#161b20;
  --white:#ffffff;
}
*{box-sizing:border-box;margin:0;padding:0}
html,body{width:1200px;height:2588px;overflow:hidden}
body{font-family:"Open Sans",Arial,sans-serif;color:var(--ink);background:var(--white);font-size:13px;line-height:1.55}
a{color:inherit;text-decoration:none}
ul{list-style:none}

/* Header */
.site-header{height:60px;display:flex;align-items:center;justify-content:space-between;padding:0 60px;background:var(--white)}
.brand{display:flex;align-items:center;gap:10px;font-family:"Open Sans",Arial,sans-serif;font-weight:700;font-size:20px;color:var(--blue-dark)}
.brand-mark{width:30px;height:30px;border-radius:50%;background:var(--blue)}
.header-tools{display:flex;gap:8px}
.header-tools span{width:16px;height:16px;border-radius:3px;background:var(--line)}

.main-nav{height:34px;background:linear-gradient(var(--blue),var(--blue-dark));display:flex;justify-content:center}
.main-nav a{display:flex;align-items:center;padding:0 38px;color:var(--white);font-size:11px;font-weight:700;letter-spacing:.5px;text-transform:uppercase}
.main-nav a.is-active{background:var(--red)}

/* Hero */
.hero{position:relative;height:406px;background:linear-gradient(120deg,#0b3e6e,#1668ad 55%,#2a86cf);overflow:hidden}
.hero-photo{position:absolute;right:0;top:0;width:620px;height:100%;background:linear-gradient(135deg,#c9d6e2,#8fa8c0 60%,#5f7f9f)}
.hero-copy{position:absolute;left:60px;top:96px;width:430px;color:var(--white)}
.hero-copy h1{font-size:36px;font-weight:800;letter-spacing:1px;margin-bottom:14px}
.hero-copy p{font-size:14px;line-height:1.6;margin-bottom:26px}
.btn{display:inline-block;background:var(--blue);color:var(--white);border-radius:16px;font-weight:600}
.btn-hero{padding:8px 26px;font-size:13px;background:#1a6fb5;border:1px solid #5aa4de}
.hero-wave{position:absolute;left:0;bottom:0;width:1200px;height:110px}

/* Section titles */
.section-title{text-align:center;font-size:26px;font-weight:600;color:var(--ink);text-transform:uppercase;letter-spacing:.5px}
.section-title::after{content:"";display:block;width:60px;height:2px;background:var(--blue);margin:8px auto 0}
.section-lead{width:820px;margin:14px auto 0;text-align:center;font-size:13px;color:var(--muted)}

/* What we do */
.services{height:400px;padding-top:34px;background:var(--white)}
.service-grid{display:flex;justify-content:center;gap:40px;margin-top:36px}
.service{width:210px;text-align:center}
.service-icon{width:72px;height:72px;margin:0 auto 12px;border-radius:50%;border:2px solid var(--line);display:flex;align-items:center;justify-content:center;background:var(--white)}
.service-icon.is-active{background:var(--blue);border-color:var(--blue)}
.service h3{font-size:11px;font-weight:700;color:var(--ink);text-transform:uppercase;line-height:1.3;margin-bottom:8px}
.service p{font-size:11px;color:var(--muted);margin-bottom:16px}
.btn-small{padding:5px 16px;font-size:10px}

/* Feature band */
.feature-band{height:300px;display:flex}
.feature-panel{width:50%;padding:36px 60px;color:var(--white)}
.feature-panel.is-blue{background:var(--blue)}
.feature-panel.is-slate{background:var(--slate)}
.feature-panel h2{font-size:22px;font-weight:600;text-transform:uppercase;margin-bottom:16px}
.tick-list li{position:relative;padding-left:22px;font-size:12px;margin-bottom:8px}
.tick-list li::before{content:"";position:absolute;left:0;top:4px;width:10px;height:10px;border-radius:50%;background:var(--white)}
.tick-list li p{font-size:11px;opacity:.8;margin-top:2px}
.feature-panel .btn{background:#135f9b;padding:5px 16px;font-size:10px;margin-top:8px}
.feature-panel.is-slate .btn{background:var(--blue)}

/* Cards */
.showcase{height:490px;padding-top:40px;background:linear-gradient(160deg,#f7f8fa,#e8ecf0)}
.card-grid{display:flex;justify-content:center;gap:24px;margin-top:30px}
.card{width:252px}
.card-media{height:150px;margin-bottom:14px}
.card h3{font-size:13px;font-weight:700;color:var(--blue);text-transform:uppercase;margin-bottom:6px}
.card p{font-size:11px;color:var(--muted);margin-bottom:12px}
.arrow-btn{width:22px;height:22px;border-radius:50%;border:2px solid var(--blue);display:flex;align-items:center;justify-content:center}

/* Testimonials */
.testimonials{height:470px;padding-top:40px;background:linear-gradient(150deg,#16446f,#245f93 50%,#1a4c7c)}
.testimonials .section-title{color:var(--white)}
.testimonials .section-title::after{background:var(--white)}
.testimonials .section-lead{color:#c8d7e6}
.quote-grid{display:flex;justify-content:center;gap:40px;margin-top:34px}
.quote{width:300px;text-align:center}
.avatar{width:64px;height:64px;margin:0 auto -20px;border-radius:50%;border:3px solid var(--white);background:linear-gradient(#b8c6d4,#7e96ad);position:relative}
.quote-body{background:var(--white);border-radius:4px;padding:30px 20px 16px;font-size:11px;color:var(--ink)}
.quote-body strong{display:block;margin-top:8px;color:var(--blue);font-size:12px}
.quote-mark{margin-top:12px;font-size:40px;line-height:1;color:var(--white);font-family:Georgia,serif}

/* Clients */
.clients{height:206px;padding-top:30px;background:var(--white)}
.client-row{display:flex;justify-content:center;gap:18px;margin-top:28px}
.client{width:180px;height:70px;border:1px solid var(--line);display:flex;align-items:center;justify-content:center;gap:8px;font-size:16px;font-weight:700;color:var(--navy)}
.client i{width:14px;height:14px;background:var(--blue);display:block}

/* Footer */
.site-footer{height:194px;background:var(--footer);color:#c3cad1;display:flex;gap:60px;padding:26px 60px 0}
.footer-col{width:240px}
.footer-col h4{font-size:12px;color:var(--white);font-weight:700;text-transform:uppercase;margin-bottom:10px}
.footer-col li{font-size:11px;line-height:1.75}
.footer-col li::before{content:"› ";color:var(--blue)}
.field{height:20px;background:#2d353e;border:1px solid #3b454f;margin-bottom:6px;font-size:10px;color:#8c959e;padding:2px 6px}
.footer-col .btn{padding:3px 14px;font-size:10px}
.social{display:flex;gap:8px}
.social span{width:26px;height:26px;border-radius:50%;background:var(--blue)}
.copyright{height:28px;background:var(--footer-deep);color:#8c959e;font-size:10px;display:flex;align-items:center;justify-content:center}
</style>
</head>
<body>

<header class="site-header">
  <a class="brand" href="#"><span class="brand-mark"></span>Quorvanta</a>
  <div class="header-tools"><span></span><span></span><span></span></div>
</header>

<nav class="main-nav">
  <a class="is-active" href="#">Home</a>
  <a href="#">Features</a>
  <a href="#">Download</a>
  <a href="#">Support</a>
  <a href="#">Purchase</a>
  <a href="#">Screenshots</a>
</nav>

<section class="hero">
  <div class="hero-photo" role="img" aria-label="Photo of a support technician with a headset working at a computer"></div>
  <svg class="hero-wave" viewBox="0 0 1200 110" preserveAspectRatio="none" aria-hidden="true">
    <path d="M0 110 L0 70 C300 110 700 20 1200 40 L1200 110 Z" fill="#ffffff"/>
    <path d="M0 70 C300 110 700 20 1200 40" fill="none" stroke="#5aa4de" stroke-width="3"/>
  </svg>
  <div class="hero-copy">
    <h1>LOREM IPSUM</h1>
    <p>Lorem Ipsum is simply dummy text of the printing and typesetting industry. Lorem Ipsum has been the industry's standard dummy text ever since.</p>
    <a class="btn btn-hero" href="#">More info</a>
  </div>
</section>

<section class="services">
  <h2 class="section-title">What We Do</h2>
  <p class="section-lead">Lorem Ipsum is simply dummy text of the printing and typesetting industry. Lorem Ipsum has been the industry's standard dummy text ever since Remaining Lorem Ipsum is simply dummy text of the printing.</p>
  <div class="service-grid">
    <div class="service">
      <div class="service-icon"><svg width="30" height="30" viewBox="0 0 30 30"><circle cx="15" cy="15" r="6" fill="none" stroke="#1b7fc9" stroke-width="3"/><path d="M15 3v5M15 22v5M3 15h5M22 15h5" stroke="#1b7fc9" stroke-width="3"/></svg></div>
      <h3>Simply<br>Dummy Text</h3>
      <p>Lorem Ipsum is simply dummy text of the printing and typesetting industry standard.</p>
      <a class="btn btn-small" href="#">Read More</a>
    </div>
    <div class="service">
      <div class="service-icon is-active"><svg width="32" height="30" viewBox="0 0 32 30"><rect x="3" y="4" width="26" height="17" rx="2" fill="none" stroke="#fff" stroke-width="2.5"/><path d="M11 26h10M16 21v5" stroke="#fff" stroke-width="2.5"/></svg></div>
      <h3>Simply<br>Dummy Text</h3>
      <p>Lorem Ipsum is simply dummy text of the printing and typesetting industry standard.</p>
      <a class="btn btn-small" href="#">Read More</a>
    </div>
    <div class="service">
      <div class="service-icon"><svg width="26" height="30" viewBox="0 0 26 30"><path d="M13 3 C13 3 4 14 4 19 a9 9 0 0 0 18 0 C22 14 13 3 13 3Z" fill="#1b7fc9"/></svg></div>
      <h3>Simply<br>Dummy Text</h3>
      <p>Lorem Ipsum is simply dummy text of the printing and typesetting industry standard.</p>
      <a class="btn btn-small" href="#">Read More</a>
    </div>
    <div class="service">
      <div class="service-icon"><svg width="28" height="30" viewBox="0 0 28 30"><circle cx="14" cy="9" r="6" fill="#1b7fc9"/><path d="M3 28c0-7 5-11 11-11s11 4 11 11Z" fill="#1b7fc9"/></svg></div>
      <h3>Simply<br>Dummy Text</h3>
      <p>Lorem Ipsum is simply dummy text of the printing and typesetting industry standard.</p>
      <a class="btn btn-small" href="#">Read More</a>
    </div>
  </div>
</section>

<section class="feature-band">
  <div class="feature-panel is-blue">
    <h2>Lorem Ipsum Is Simply Dummy Text</h2>
    <ul class="tick-list">
      <li>Lorem Ipsum is simply dummy text of</li>
      <li>Lorem Ipsum is simply dummy text</li>
      <li>Lorem Ipsum is simply dummy text of the printing</li>
      <li>Lorem Ipsum is simply dummy text of</li>
      <li>Lorem Ipsum is simply dummy text of the</li>
    </ul>
    <a class="btn" href="#">Read More</a>
  </div>
  <div class="feature-panel is-slate">
    <h2>Lorem Ipsum Is Simply</h2>
    <ul class="tick-list">
      <li>Lorem Ipsum is simply dummy text of<p>Lorem Ipsum is simply dummy text of the printing and typesetting industry standard.</p></li>
      <li>Lorem Ipsum is simply dummy text<p>Lorem Ipsum is simply dummy text of the printing and typesetting industry.</p></li>
      <li>Lorem Ipsum is simply dummy text of</li>
    </ul>
    <a class="btn" href="#">Read More</a>
  </div>
</section>

<section class="showcase">
  <h2 class="section-title">Lorem Ipsum Is Simply Dummy Text</h2>
  <p class="section-lead">Lorem Ipsum is simply dummy text of the printing and typesetting industry. Lorem Ipsum has been the industry's standard dummy text ever since Remaining Lorem Ipsum is simply dummy text of the printing and typesetting.</p>
  <div class="card-grid">
    <article class="card">
      <div class="card-media" role="img" aria-label="Photo of hands pointing at a chart on a tablet" style="background:linear-gradient(135deg,#9fb8cf,#4d79a3)"></div>
      <h3>Lorem Ipsum Simply</h3>
      <p>Lorem Ipsum is simply dummy text of the printing and typesetting industry. Lorem Ipsum has been the standard dummy text.</p>
      <a class="arrow-btn" href="#"><svg width="10" height="10" viewBox="0 0 10 10"><path d="M3 1l4 4-4 4" fill="none" stroke="#1b7fc9" stroke-width="2"/></svg></a>
    </article>
    <article class="card">
      <div class="card-media" role="img" aria-label="Photo of computer hardware components" style="background:linear-gradient(135deg,#c4c9ce,#6e757c)"></div>
      <h3>Lorem Ipsum Simply</h3>
      <p>Lorem Ipsum is simply dummy text of the printing and typesetting industry. Lorem Ipsum has been the standard dummy text.</p>
      <a class="arrow-btn" href="#"><svg width="10" height="10" viewBox="0 0 10 10"><path d="M3 1l4 4-4 4" fill="none" stroke="#1b7fc9" stroke-width="2"/></svg></a>
    </article>
    <article class="card">
      <div class="card-media" role="img" aria-label="Photo of a repair service sign on a workbench" style="background:linear-gradient(135deg,#8fa06a,#3f4a37)"></div>
      <h3>Lorem Ipsum Simply</h3>
      <p>Lorem Ipsum is simply dummy text of the printing and typesetting industry. Lorem Ipsum has been the standard dummy text.</p>
      <a class="arrow-btn" href="#"><svg width="10" height="10" viewBox="0 0 10 10"><path d="M3 1l4 4-4 4" fill="none" stroke="#1b7fc9" stroke-width="2"/></svg></a>
    </article>
    <article class="card">
      <div class="card-media" role="img" aria-label="Photo of two business people shaking hands in an office" style="background:linear-gradient(135deg,#d6dde4,#7f93a7)"></div>
      <h3>Lorem Ipsum Simply</h3>
      <p>Lorem Ipsum is simply dummy text of the printing and typesetting industry. Lorem Ipsum has been the standard dummy text.</p>
      <a class="arrow-btn" href="#"><svg width="10" height="10" viewBox="0 0 10 10"><path d="M3 1l4 4-4 4" fill="none" stroke="#1b7fc9" stroke-width="2"/></svg></a>
    </article>
  </div>
</section>

<section class="testimonials">
  <h2 class="section-title">Testimonials</h2>
  <p class="section-lead">Lorem Ipsum is simply dummy text of the printing and typesetting industry. Lorem Ipsum has been the industry's standard dummy text ever since Remaining Lorem Ipsum is simply dummy text of the printing and typesetting.</p>
  <div class="quote-grid">
    <div class="quote">
      <div class="avatar" role="img" aria-label="Customer portrait"></div>
      <div class="quote-body">Lorem Ipsum is simply dummy text of the printing and typesetting industry. Lorem Ipsum has been the industry's standard dummy text ever since.<strong>Anna Kerr</strong></div>
      <div class="quote-mark">&ldquo;</div>
    </div>
    <div class="quote">
      <div class="avatar" role="img" aria-label="Customer portrait"></div>
      <div class="quote-body">Lorem Ipsum is simply dummy text of the printing and typesetting industry. Lorem Ipsum has been the industry's standard dummy text ever since.<strong>Mark Ellis</strong></div>
      <div class="quote-mark">&ldquo;</div>
    </div>
    <div class="quote">
      <div class="avatar" role="img" aria-label="Customer portrait"></div>
      <div class="quote-body">Lorem Ipsum is simply dummy text of the printing and typesetting industry. Lorem Ipsum has been the industry's standard dummy text ever since.<strong>Paul Hayes</strong></div>
      <div class="quote-mark">&ldquo;</div>
    </div>
  </div>
</section>

<section class="clients">
  <h2 class="section-title">Our Client</h2>
  <div class="client-row">
    <div class="client"><i></i>Norvex</div>
    <div class="client">Tidewell</div>
    <div class="client">Brightcode</div>
    <div class="client">Company Name</div>
    <div class="client">Ironvale</div>
  </div>
</section>

<footer class="site-footer">
  <div class="footer-col">
    <h4>Main Menu</h4>
    <ul><li>Home</li><li>Features</li><li>Download</li><li>Support</li><li>Purchase</li><li>Screenshots</li></ul>
  </div>
  <div class="footer-col">
    <h4>Quick Links</h4>
    <ul><li>Customer Policy</li><li>Booking</li><li>Terms and Conditions</li><li>Privacy Policy</li><li>Contact</li></ul>
  </div>
  <div class="footer-col">
    <h4>Newsletter</h4>
    <div class="field">Your Name</div>
    <div class="field">Email Address</div>
    <a class="btn" href="#">Subscribe</a>
  </div>
  <div class="footer-col">
    <h4>Get In Touch</h4>
    <div class="social"><span></span><span></span><span></span></div>
  </div>
</footer>
<div class="copyright">Copyright &copy; 2015 Quorvanta. All rights reserved. Privacy Policy | Terms of Use | Contact</div>

</body>
</html>
```